Kel. Harbors, inc.

I want to publish a website directed at IL business owners with the objective of offering several modules and links highlighting specific topics:
1- economic incentives from various states
2- current economic comparisons between the states with regard to taxes, logistics, regulations, business climate.
3- feature a successful entrepreneur and how he is dealing with the current load of regulations
4- companies moving out of state, where and why
5- pending legislation that would have an impact on business
6- websites, contact information from various states for businesses to contact.
A wide ranging and continuous source of options, information and inspiration for business owners.
Industry/Entity Type
Business
Requirements
Must have
- -Need map graphs and some interactive calculators
-open block for an open question allowing reader to put up an answer.

```html
<!DOCTYPE html>
<html lang="en">
<head>
<meta charset="utf-8">
<title>Kel. Harbors, inc.</title>
<link href="https://fonts.googleapis.com/css2?family=Open+Sans:wght@400;600&display=swap" rel="stylesheet">
<style>
:root{
  --ink:#2b2b2b;
  --topbar:#2a2a2a;
  --header:#ececec;
  --nav:#efefef;
  --line:#d4d4d4;
  --panel:#e7e7e7;
  --band:#e9e9e9;
  --link:#2f6d8f;
  --muted:#555;
  --accent-green:#7fd08f;
  --accent-blue:#7f9be0;
  --orange-top:#f0b955;
  --orange-bottom:#e2992f;
  --footer:#262626;
  --footer-text:#d8d8d8;
  --footer-active:#4a8fc0;
}
*{box-sizing:border-box;margin:0;padding:0}
html,body{width:1200px;height:2196px;overflow:hidden}
body{position:relative;background:#fff;font-family:"Open Sans",Arial,sans-serif;color:var(--ink)}
.abs{position:absolute}

/* top bar */
.topbar{left:0;top:0;width:1200px;height:41px;background:var(--topbar)}
.toplinks{position:absolute;top:13px;font-size:12px;color:#eee}
.search{position:absolute;left:878px;top:8px;width:160px;height:26px;background:#fff;border:1px solid #bbb;font-size:11px;color:#444;padding:5px 7px}
.search svg{position:absolute;right:6px;top:5px}

/* header */
.site-header{left:0;top:41px;width:1200px;height:72px;background:var(--header)}
.brand{position:absolute;left:135px;top:19px;font-family:"Open Sans",Arial,sans-serif;font-weight:600;font-size:27px;line-height:34px;color:#1e1e1e}

/* nav */
.mainnav{left:0;top:113px;width:1200px;height:38px;background:var(--nav);border-top:1px solid #d8d8d8;border-bottom:1px solid #c9c9c9;box-shadow:0 2px 3px rgba(0,0,0,.08)}
.nav-item{position:absolute;top:0;height:37px;line-height:37px;font-size:12px;color:#333;text-align:center;border-left:1px solid #d2d2d2}
.nav-home{left:135px;width:36px}

/* chart & login */
.chart-panel{left:135px;top:176px;width:609px;height:274px;border:1px solid #e2e2e2;background:#fff}
.login-panel{left:765px;top:176px;width:285px;height:274px;background:#f1f1f1;border:1px solid #dcdcdc;border-radius:4px;box-shadow:0 1px 3px rgba(0,0,0,.12)}
.field{position:absolute;left:26px;width:231px;height:42px;background:#dedede;border:1px solid #cfcfcf;font-size:15px;color:#555;padding:10px 16px}
.login-btn{position:absolute;left:26px;top:197px;width:231px;height:47px;border-radius:3px;background:linear-gradient(var(--orange-top),var(--orange-bottom));border:1px solid #cf8a25;color:#fff;font-size:17px;font-weight:600;text-align:center;line-height:45px}

/* sections */
.section{left:135px;width:915px;height:234px}
.section-head{position:absolute;left:0;top:0;width:915px;height:39px;background:var(--band);font-size:15px;color:#222;padding:10px 17px}
.more{position:absolute;right:17px;top:10px;font-size:14px;color:#333}
.chev{display:inline-block;width:19px;height:19px;border-radius:50%;background:#3c3c3c;vertical-align:middle;position:relative;margin-left:8px;top:-1px}
.chev::after{content:"";position:absolute;left:6px;top:4px;width:5px;height:5px;border-right:2px solid #fff;border-bottom:2px solid #fff;transform:rotate(45deg)}
.chev.small{width:17px;height:17px;margin-left:5px}
.chev.small::after{left:5px;top:3px}
.card{position:absolute;top:55px;width:293px;height:178px;background:var(--panel);border:1px solid #d6d6d6}
.card-media{position:absolute;left:2px;top:2px;width:287px;height:125px}
.media-globe{background:linear-gradient(120deg,#3b4e63 0%,#6fa6c2 45%,#8fc5db 60%,#4a5866 100%)}
.media-office{background:linear-gradient(90deg,#ffffff 0%,#fafafa 55%,#e8c7c8 72%,#f4f4f4 100%)}
.media-car{background:radial-gradient(ellipse at 60% 55%,#5a5a5a 0%,#222 35%,#000 70%)}
.card-title{position:absolute;left:12px;top:131px;font-size:13px;color:var(--link)}
.card-date{position:absolute;left:12px;top:151px;font-size:10px;color:#444}
.details{position:absolute;right:10px;top:137px;font-size:11px;color:#444}

/* contacts */
.contacts{left:135px;top:1798px;width:915px;height:226px;background:var(--band)}
.contacts .section-head{background:#e3e3e3}
.select-state{position:absolute;left:773px;top:9px;width:124px;height:25px;background:#777;color:#eee;font-size:11px;padding:5px 17px;border-radius:2px}
.select-state .divider{position:absolute;left:88px;top:5px;width:1px;height:15px;background:#aaa}
.select-state .chev{position:absolute;right:6px;top:4px;margin:0;width:17px;height:17px;background:#444}
.select-state .chev::after{left:5px;top:3px}
.contact{position:absolute;font-size:12.5px;line-height:17px;color:#222}
.contact .name{color:var(--link);font-weight:600}
.contact-arrow{position:absolute;left:-18px;top:4px}

/* footer */
.site-footer{left:0;top:2064px;width:1200px;height:132px;background:var(--footer)}
.footnav{position:absolute;top:22px;width:1200px;text-align:center;font-size:12px;color:var(--footer-text);word-spacing:2px}
.footnav span{margin:0 10px}
.footnav .active{color:var(--footer-active)}
.copyright{position:absolute;top:48px;width:1200px;text-align:center;font-size:11px;color:var(--footer-text)}
.social{position:absolute;top:86px;width:22px;height:22px;border-radius:2px}
</style>
</head>
<body>

<div class="abs topbar">
  <span class="toplinks" style="left:612px">What is new</span>
  <span class="toplinks" style="left:714px">Hot topics <span style="font-size:9px">▾</span></span>
  <span class="toplinks" style="left:805px">Join Us</span>
  <div class="search">Search here...
    <svg width="15" height="15" viewBox="0 0 15 15"><circle cx="9" cy="6" r="4.5" fill="none" stroke="#555" stroke-width="1.6"/><line x1="6" y1="9" x2="1.5" y2="13.5" stroke="#555" stroke-width="2"/></svg>
  </div>
</div>

<header class="abs site-header">
  <div class="brand">Kel. Harbors, inc.</div>
</header>

<nav class="abs mainnav">
  <div class="nav-item nav-home" style="border-left:none">
    <svg width="20" height="18" viewBox="0 0 20 18" style="margin-top:10px"><path d="M10 1 L19 9 H16 V17 H12 V12 H8 V17 H4 V9 H1 Z" fill="#3a7ea8"/></svg>
  </div>
  <div class="nav-item" style="left:171px;width:207px">STATE ECONOMIC DEPARTMENTS</div>
  <div class="nav-item" style="left:378px;width:130px">TAX COMPARISONS</div>
  <div class="nav-item" style="left:508px;width:156px">COMPANY MOVEMENTS</div>
  <div class="nav-item" style="left:664px;width:81px">ABOUT US</div>
  <div class="nav-item" style="left:745px;width:99px">OUR SERVICES</div>
  <div class="nav-item" style="left:844px;width:97px">CONTACT US</div>
  <div class="nav-item" style="left:941px;width:54px;border-right:1px solid #d2d2d2">MORE</div>
</nav>

<div class="abs chart-panel">
  <svg width="607" height="272" viewBox="0 0 607 272" font-family="Open Sans, Arial, sans-serif" font-size="10" fill="#888">
    <g stroke="#e6e6e6" stroke-width="1">
      <line x1="63" y1="28" x2="580" y2="28"/><line x1="63" y1="80" x2="580" y2="80"/>
      <line x1="63" y1="132" x2="580" y2="132"/><line x1="63" y1="184" x2="580" y2="184"/>
      <line x1="63" y1="235" x2="580" y2="235"/>
      <line x1="70" y1="28" x2="70" y2="235"/><line x1="177" y1="28" x2="177" y2="235"/>
      <line x1="279" y1="28" x2="279" y2="235"/><line x1="381" y1="28" x2="381" y2="235"/>
      <line x1="486" y1="28" x2="486" y2="235"/>
    </g>
    <text x="22" y="31">8000</text><text x="22" y="83">6000</text>
    <text x="22" y="135">4000</text><text x="22" y="187">2000</text>
    <text x="63" y="252">May</text><text x="169" y="252">June</text><text x="271" y="252">July</text>
    <text x="375" y="252">Aug</text><text x="477" y="252">Sept</text>
    <path d="M63 144 L136 116 L188 139 L241 100 L298 114 L354 91 L406 131 L467 47 L533 97 L579 61 L579 235 L63 235 Z" fill="#7fd08f" fill-opacity=".18"/>
    <path d="M63 216 L111 200 L165 208 L218 174 L271 193 L318 169 L387 207 L456 168 L538 147 L579 155 L579 235 L63 235 Z" fill="#7fc2e0" fill-opacity=".28"/>
    <polyline points="63,144 136,116 188,139 241,100 298,114 354,91 406,131 467,47 533,97 579,61" fill="none" stroke="#7fd08f" stroke-width="2"/>
    <polyline points="63,216 111,200 165,208 218,174 271,193 318,169 387,207 456,168 538,147 579,155" fill="none" stroke="#7f9be0" stroke-width="2"/>
    <g fill="#fff" stroke="#7fd08f" stroke-width="2">
      <circle cx="136" cy="116" r="4.5"/><circle cx="188" cy="139" r="4.5"/><circle cx="241" cy="100" r="4.5"/>
      <circle cx="298" cy="114" r="4.5"/><circle cx="354" cy="91" r="6"/><circle cx="406" cy="131" r="4.5"/>
      <circle cx="467" cy="47" r="4.5"/><circle cx="533" cy="97" r="4.5"/>
    </g>
    <g fill="#fff" stroke="#7f9be0" stroke-width="2">
      <circle cx="111" cy="200" r="4.5"/><circle cx="165" cy="208" r="4.5"/><circle cx="218" cy="174" r="4.5"/>
      <circle cx="271" cy="193" r="4.5"/><circle cx="318" cy="169" r="4.5"/><circle cx="387" cy="207" r="4.5"/>
      <circle cx="456" cy="168" r="4.5"/><circle cx="538" cy="147" r="4.5"/>
    </g>
    <rect x="318" y="48" width="74" height="27" fill="#3a3a3a"/>
    <path d="M349 75 L355 81 L361 75 Z" fill="#3a3a3a"/>
    <text x="355" y="66" fill="#fff" font-size="11" text-anchor="middle">25471</text>
  </svg>
</div>

<div class="abs login-panel">
  <svg width="283" height="60" viewBox="0 0 283 60" style="position:absolute;left:0;top:0">
    <g fill="none" stroke="#b9b9b9" stroke-width="3">
      <path d="M33 30 V18 a5 5 0 0 1 10 0 V30"/><path d="M88 30 V18 a5 5 0 0 1 10 0 V30"/>
      <path d="M143 30 V18 a5 5 0 0 1 10 0 V30"/><path d="M198 30 V18 a5 5 0 0 1 10 0 V30"/>
      <path d="M253 30 V18 a5 5 0 0 1 10 0 V30"/>
    </g>
    <g fill="#cfcfcf"><circle cx="38" cy="33" r="4"/><circle cx="93" cy="33" r="4"/><circle cx="148" cy="33" r="4"/><circle cx="203" cy="33" r="4"/><circle cx="258" cy="33" r="4"/></g>
  </svg>
  <div class="field" style="top:83px">Username</div>
  <div class="field" style="top:125px">Password</div>
  <div class="login-btn">Log in</div>
</div>

<section class="abs section" style="top:474px">
  <div class="section-head">Economic incentives from various states<span class="more">More<span class="chev"></span></span></div>
  <div class="card" style="left:2px"><div class="card-media media-globe" role="img" aria-label="Photo of a hand touching a glowing world map with connection lines"></div><div class="card-title">Matter headline goes here.</div><div class="card-date">Feb. 12, 2013 08.15 CST</div><div class="details">Details<span class="chev small"></span></div></div>
  <div class="card" style="left:311px"><div class="card-media media-office" role="img" aria-label="Photo of a businessman working at a laptop"></div><div class="card-title">Matter headline goes here.</div><div class="card-date">Feb. 12, 2013 08.15 CST</div><div class="details">Details<span class="chev small"></span></div></div>
  <div class="card" style="left:620px"><div class="card-media media-car" role="img" aria-label="Photo of a silver sports car on a black background"></div><div class="card-title">Matter headline goes here.</div><div class="card-date">Feb. 12, 2013 08.15 CST</div><div class="details">Details<span class="chev small"></span></div></div>
</section>

<section class="abs section" style="top:737px">
  <div class="section-head">Current economic comparisons between the states<span class="more">More<span class="chev"></span></span></div>
  <div class="card" style="left:2px"><div class="card-media media-globe" role="img" aria-label="Photo of a hand touching a glowing world map with connection lines"></div><div class="card-title">Matter headline goes here.</div><div class="card-date">Feb. 12, 2013 08.15 CST</div><div class="details">Details<span class="chev small"></span></div></div>
  <div class="card" style="left:311px"><div class="card-media media-office" role="img" aria-label="Photo of a businessman working at a laptop"></div><div class="card-title">Matter headline goes here.</div><div class="card-date">Feb. 12, 2013 08.15 CST</div><div class="details">Details<span class="chev small"></span></div></div>
  <div class="card" style="left:620px"><div class="card-media media-car" role="img" aria-label="Photo of a silver sports car on a black background"></div><div class="card-title">Matter headline goes here.</div><div class="card-date">Feb. 12, 2013 08.15 CST</div><div class="details">Details<span class="chev small"></span></div></div>
</section>

<section class="abs section" style="top:1001px">
  <div class="section-head">Feature a successful entrepreneur<span class="more">More<span class="chev"></span></span></div>
  <div class="card" style="left:2px"><div class="card-media media-globe" role="img" aria-label="Photo of a hand touching a glowing world map with connection lines"></div><div class="card-title">Matter headline goes here.</div><div class="card-date">Feb. 12, 2013 08.15 CST</div><div class="details">Details<span class="chev small"></span></div></div>
  <div class="card" style="left:311px"><div class="card-media media-office" role="img" aria-label="Photo of a businessman working at a laptop"></div><div class="card-title">Matter headline goes here.</div><div class="card-date">Feb. 12, 2013 08.15 CST</div><div class="details">Details<span class="chev small"></span></div></div>
  <div class="card" style="left:620px"><div class="card-media media-car" role="img" aria-label="Photo of a silver sports car on a black background"></div><div class="card-title">Matter headline goes here.</div><div class="card-date">Feb. 12, 2013 08.15 CST</div><div class="details">Details<span class="chev small"></span></div></div>
</section>

<section class="abs section" style="top:1264px">
  <div class="section-head">Companies moving out of state, where and why<span class="more">More<span class="chev"></span></span></div>
  <div class="card" style="left:2px"><div class="card-media media-globe" role="img" aria-label="Photo of a hand touching a glowing world map with connection lines"></div><div class="card-title">Matter headline goes here.</div><div class="card-date">Feb. 12, 2013 08.15 CST</div><div class="details">Details<span class="chev small"></span></div></div>
  <div class="card" style="left:311px"><div class="card-media media-office" role="img" aria-label="Photo of a businessman working at a laptop"></div><div class="card-title">Matter headline goes here.</div><div class="card-date">Feb. 12, 2013 08.15 CST</div><div class="details">Details<span class="chev small"></span></div></div>
  <div class="card" style="left:620px"><div class="card-media media-car" role="img" aria-label="Photo of a silver sports car on a black background"></div><div class="card-title">Matter headline goes here.</div><div class="card-date">Feb. 12, 2013 08.15 CST</div><div class="details">Details<span class="chev small"></span></div></div>
</section>

<section class="abs section" style="top:1531px">
  <div class="section-head">Pending legislation<span class="more">More<span class="chev"></span></span></div>
  <div class="card" style="left:2px"><div class="card-media media-globe" role="img" aria-label="Photo of a hand touching a glowing world map with connection lines"></div><div class="card-title">Matter headline goes here.</div><div class="card-date">Feb. 12, 2013 08.15 CST</div><div class="details">Details<span class="chev small"></span></div></div>
  <div class="card" style="left:311px"><div class="card-media media-office" role="img" aria-label="Photo of a businessman working at a laptop"></div><div class="card-title">Matter headline goes here.</div><div class="card-date">Feb. 12, 2013 08.15 CST</div><div class="details">Details<span class="chev small"></span></div></div>
  <div class="card" style="left:620px"><div class="card-media media-car" role="img" aria-label="Photo of a silver sports car on a black background"></div><div class="card-title">Matter headline goes here.</div><div class="card-date">Feb. 12, 2013 08.15 CST</div><div class="details">Details<span class="chev small"></span></div></div>
</section>

<section class="abs contacts">
  <div class="section-head">Websites &amp; contact information
    <div class="select-state">Select State<span class="divider"></span><span class="chev"></span></div>
  </div>
  <div class="contact" style="left:56px;top:57px"><svg class="contact-arrow" width="10" height="10" viewBox="0 0 10 10"><path d="M1 1 L9 5 L1 9 L3 5 Z" fill="#333"/></svg><div class="name">Business / Company Name</div>www.agencylink.org<br>12/b, Cedar lane, IL<br>Ph : 555 - 0148 - 210</div>
  <div class="contact" style="left:276px;top:57px"><svg class="contact-arrow" width="10" height="10" viewBox="0 0 10 10"><path d="M1 1 L9 5 L1 9 L3 5 Z" fill="#333"/></svg><div class="name">Business / Company Name</div>www.agencylink.org<br>12/b, Cedar lane, IL<br>Ph : 555 - 0148 - 210</div>
  <div class="contact" style="left:496px;top:57px"><svg class="contact-arrow" width="10" height="10" viewBox="0 0 10 10"><path d="M1 1 L9 5 L1 9 L3 5 Z" fill="#333"/></svg><div class="name">Business / Company Name</div>www.agencylink.org<br>12/b, Cedar lane, IL<br>Ph : 555 - 0148 - 210</div>
  <div class="contact" style="left:714px;top:57px"><svg class="contact-arrow" width="10" height="10" viewBox="0 0 10 10"><path d="M1 1 L9 5 L1 9 L3 5 Z" fill="#333"/></svg><div class="name">Business / Company Name</div>www.agencylink.org<br>12/b, Cedar lane, IL<br>Ph : 555 - 0148 - 210</div>
  <div class="contact" style="left:56px;top:137px"><svg class="contact-arrow" width="10" height="10" viewBox="0 0 10 10"><path d="M1 1 L9 5 L1 9 L3 5 Z" fill="#333"/></svg><div class="name">Business / Company Name</div>www.agencylink.org<br>12/b, Cedar lane, IL<br>Ph : 555 - 0148 - 210</div>
  <div class="contact" style="left:276px;top:137px"><svg class="contact-arrow" width="10" height="10" viewBox="0 0 10 10"><path d="M1 1 L9 5 L1 9 L3 5 Z" fill="#333"/></svg><div class="name">Business / Company Name</div>www.agencylink.org<br>12/b, Cedar lane, IL<br>Ph : 555 - 0148 - 210</div>
  <div class="contact" style="left:496px;top:137px"><svg class="contact-arrow" width="10" height="10" viewBox="0 0 10 10"><path d="M1 1 L9 5 L1 9 L3 5 Z" fill="#333"/></svg><div class="name">Business / Company Name</div>www.agencylink.org<br>12/b, Cedar lane, IL<br>Ph : 555 - 0148 - 210</div>
  <div class="contact" style="left:714px;top:137px"><svg class="contact-arrow" width="10" height="10" viewBox="0 0 10 10"><path d="M1 1 L9 5 L1 9 L3 5 Z" fill="#333"/></svg><div class="name">Business / Company Name</div>www.agencylink.org<br>12/b, Cedar lane, IL<br>Ph : 555 - 0148 - 210</div>
</section>

<footer class="abs site-footer">
  <div class="footnav"><span class="active">HOME</span><span>STATE ECONOMIC DEPARTMENTS</span><span>TAX COMPARISONS</span><span>COMPANY MOVEMENTS</span><span>ABOUT US</span><span>OUR SERVICES</span><span>CONTACT US</span><span>MORE</span></div>
  <div class="copyright">COPYRIGHT @ 2013, KEL. HARBORS INC. ALL RIGHTS ARE RESERVED.</div>
  <div class="social" style="left:565px;background:#3f9bb8"></div>
  <div class="social" style="left:590px;background:#3b62a8"></div>
  <div class="social" style="left:615px;background:#9a8a5a"></div>
</footer>

</body>
</html>
```